Etiketten-Design für Honig
Zielgruppe
Flinker Honig aus dem Bayerischen Wald
Bio
Waldhonig sowie Honig mit Zusätzen wie Bio-Himbeere, Bio-Erdbeere usw.
Aufgabenstellung
Bär, Bayrischer Wald, Bio Nr. und natürlich Honig
Modern und cool

```html
<!DOCTYPE html>
<html lang="de">
<head>
<meta charset="utf-8">
<title>Flinker Honig – Etikett</title>
<link rel="stylesheet" href="https://fonts.googleapis.com/css2?family=Quicksand:wght@300;500&family=Yellowtail&display=swap">
<style>
  :root {
    --band: #e2b33a;
    --band-edge: #7a6a5a;
    --frame-edge: #5e4a3e;
    --paper: #ffffff;
    --honey-light: #fad22a;
    --honey-deep: #e6b02f;
    --ink: #5b3a34;
    --bio-green: #1f5d2a;
    --forest: #2a6a3a;
  }
  html, body {
    margin: 0;
    padding: 0;
    width: 1200px;
    height: 524px;
    overflow: hidden;
    background: var(--paper);
  }
  .label {
    display: block;
    width: 1200px;
    height: 524px;
  }
  .band { fill: var(--band); stroke: var(--band-edge); stroke-width: 2.5; }
  .frame-outer { fill: var(--paper); stroke: var(--frame-edge); stroke-width: 2.5; }
  .frame-inner { fill: url(#honeyFill); stroke: var(--frame-edge); stroke-width: 2; stroke-dasharray: 7 5; }
  .title-light {
    font-family: "Quicksand", sans-serif;
    font-weight: 300;
    font-size: 33px;
    fill: var(--ink);
  }
  .title-script {
    font-family: "Yellowtail", cursive;
    font-size: 72px;
    fill: var(--ink);
  }
  .origin {
    font-family: "Quicksand", sans-serif;
    font-weight: 300;
    font-size: 32px;
    fill: var(--ink);
  }
  .bio {
    font-family: "Quicksand", sans-serif;
    font-weight: 500;
    font-size: 33px;
    fill: var(--bio-green);
  }
</style>
</head>
<body>
<svg class="label" viewBox="0 0 1200 524" xmlns="http://www.w3.org/2000/svg">
  <defs>
    <linearGradient id="honeyFill" x1="0" y1="0" x2="1" y2="0">
      <stop offset="0" stop-color="var(--honey-light)"/>
      <stop offset="1" stop-color="var(--honey-deep)"/>
    </linearGradient>
    <radialGradient id="sceneFill" cx="0.5" cy="0.5" r="0.6">
      <stop offset="0" stop-color="#d9a21c"/>
      <stop offset="0.55" stop-color="#9a7a2c"/>
      <stop offset="1" stop-color="var(--forest)" stop-opacity="0.85"/>
    </radialGradient>
  </defs>

  <rect class="band" x="2" y="105" width="1196" height="313" rx="20" ry="20"/>

  <polygon class="frame-outer" points="449,2 750,2 901,262 750,522 449,522 300,262"/>
  <polygon class="frame-inner" points="459,24 739,24 876,262 739,500 459,500 324,262"/>

  <rect class="scene" x="441" y="47" width="320" height="208" rx="30"
        fill="url(#sceneFill)" role="img"
        aria-label="Illustration: Bienenkorb zwischen zwei Tannen mit einer Biene"/>

  <g class="product-name">
    <text class="title-light" x="488" y="323">Flinker</text>
    <text class="title-script" x="595" y="325">Honig</text>
  </g>
  <text class="origin" x="605" y="375" text-anchor="middle">aus dem Bayerischen Wald</text>
  <text class="bio" x="603" y="431" text-anchor="middle">BIO</text>
</svg>
</body>
</html>
```